Adult Literacy Program - flyer to attract volunteers and students

We want a flyer that is engaging, colorful, modern and will appeal to our primary audience of adults aged 40-60. We are trying to attract both prospective volunteers (typically age 50+, mostly women) and students (typically aged 40+).
The flyer should feature diverse people working together in pairs of two, reading or talking, with a workbook or some reading material in front of them.

Our organization trains tutors to work one-on-one with adults who are learning how to read. Most of our adult students are non-native speakers of English. Many are of Haitian or Hispanic origin, so we would like some people who represent that demographic.

The Flyer should represent reading, learning, literacy, knowledge, growth,
and opportunities.
Our students are learning to read so they can advance their job opportunities.

Target Market(s)

Adults aged 40-60, primarily women, retired, volunteers

Industry/Entity Type

Education

Font styles to use
Serif
Sans Serif

Colors

Designer to choose colors to be used in the design.

Requirements
Must have
• - UPDATE: Should be designed as a TRI-FOLD brochure on 8.5 x 11 inch paper that will be folded into thirds.
• - Images of diverse people, women and men, who look Hispanic, Haitian and other nationalities as well as Caucasian.
• - Our logo on the front cover
Nice to have
• The sample flyer is very boring and dry! We are open to different ways of presenting the text.

```html
<!DOCTYPE html>
<html lang="en">
<head>
<meta charset="utf-8">
<title>Volunteer Flyer</title>
<link href="https://fonts.googleapis.com/css2?family=Roboto+Condensed:wght@400;700&family=Arimo:wght@400;700&family=PT+Sans&display=swap" rel="stylesheet">
<style>
  :root{
    --page-bg:#707372;
    --navy:#4153a4;
    --cyan:#00a9dc;
    --orange:#f7902a;
    --white:#ffffff;
    --photo-a:#a98a6e;
    --photo-b:#c9b9a4;
    --photo-c:#6f86a6;
  }
  *{margin:0;padding:0;box-sizing:border-box}
  html,body{width:1200px;height:1200px;overflow:hidden;background:var(--page-bg)}
  .flyer-wrap{position:absolute;left:168px;top:40px;width:865px;height:1120px;box-shadow:0 8px 24px rgba(0,0,0,.35)}
  .flyer{position:absolute;left:0;top:0;width:976px;height:1264px;transform:scale(0.8862);transform-origin:0 0;background:var(--white);overflow:hidden;font-family:"Arimo",Arial,sans-serif;color:var(--white)}
  .flyer-shapes{position:absolute;inset:0}
  .brand{position:absolute;left:700px;top:72px;display:flex;align-items:center;gap:10px;color:var(--navy);font-weight:700;font-size:17px;letter-spacing:.5px;white-space:nowrap}
  .brand-dot{width:16px;height:16px;border-radius:50%;background:var(--navy);flex:none}

  .tutors{position:absolute;left:15px;top:611px;width:420px;height:354px;background:var(--navy);border-radius:26px;padding:12px 0 0 24px}
  .tutors h2{font-family:"Roboto Condensed",sans-serif;font-weight:400;color:var(--orange);font-size:42px;line-height:46px;margin-bottom:11px}
  .tutors ul{list-style:none;font-size:18px;line-height:23px}
  .tutors li{position:relative;padding-left:16px;margin-bottom:5px;white-space:nowrap}
  .tutors li::before{content:"•";position:absolute;left:0;top:0;font-size:13px}
  .tutors .tagline{font-weight:700;font-size:18px;line-height:23px;margin-top:1px;white-space:nowrap}

  .cta{position:absolute;left:15px;top:979px;width:420px;height:185px;background:var(--orange);border-radius:22px;padding:59px 0 0 24px;font-size:21px;line-height:27px;white-space:nowrap}
  .cta strong{display:block}

  .circle-photo{position:absolute;border-radius:50%;border:5px solid var(--orange);box-shadow:0 0 0 6px var(--white)}
  .circle-1{left:353px;top:564px;width:164px;height:164px;background:radial-gradient(circle at 45% 40%,var(--photo-b),var(--photo-a) 70%)}
  .circle-2{left:348px;top:750px;width:174px;height:174px;background:radial-gradient(circle at 50% 45%,var(--photo-b),var(--photo-c) 75%)}
  .circle-3{left:358px;top:949px;width:166px;height:166px;background:radial-gradient(circle at 50% 45%,#d7b9a6,#9a5a5a 75%)}

  .intro{position:absolute;right:40px;top:555px;text-align:right;font-family:"Roboto Condensed",sans-serif;white-space:nowrap}
  .intro h1{color:var(--orange);font-weight:400;font-size:74px;line-height:84px;letter-spacing:-1px}
  .intro p{font-size:40px;line-height:52px}
  .intro .first{margin-top:6px}

  .students{position:absolute;right:34px;top:821px;text-align:right;white-space:nowrap}
  .students h2{font-family:"Roboto Condensed",sans-serif;font-weight:700;font-size:38px;line-height:46px;margin-bottom:14px;padding-right:12px}
  .students .lead{font-size:18.5px;line-height:24px;margin-bottom:4px;padding-right:20px}
  .students ul{list-style:none;font-size:18.5px;line-height:23px}
  .students li::after{content:"";display:inline-block;width:8px;height:8px;border-radius:50%;background:var(--white);margin-left:10px;vertical-align:-1px}
  .students .tagline{font-weight:700;font-size:21px;line-height:26px;margin-top:13px;padding-right:20px}

  .contact{position:absolute;left:0;width:960px;top:1166px;text-align:center;font-family:"PT Sans",sans-serif;font-size:17px;line-height:24px}
  .contact .mail{display:inline-flex;align-items:center;gap:8px;margin-top:2px}
</style>
</head>
<body>
<div class="flyer-wrap">
  <div class="flyer">
    <svg class="flyer-shapes" viewBox="0 0 976 1264" width="976" height="1264">
      <defs>
        <linearGradient id="mainPhoto" x1="0" y1="0" x2="1" y2="1">
          <stop offset="0" stop-color="#8b6f52"/>
          <stop offset=".45" stop-color="#c7b49c"/>
          <stop offset="1" stop-color="#7d93b3"/>
        </linearGradient>
      </defs>
      <path role="img" aria-label="Photo: a diverse group of adults reading books together around a library table"
            d="M0,0 H340 C520,110 780,150 976,150 V500 C800,520 600,525 440,540 C260,555 110,480 0,385 Z" fill="url(#mainPhoto)"/>
      <path d="M340,0 C520,110 780,150 976,150" fill="none" stroke="var(--cyan)" stroke-width="14"/>
      <path d="M372,0 C540,95 790,138 976,138" fill="none" stroke="var(--white)" stroke-width="6"/>
      <path d="M0,395 C110,490 260,565 410,590" fill="none" stroke="var(--cyan)" stroke-width="14"/>
      <path d="M438,545 C600,528 800,520 976,500 V1264 H438 Z" fill="var(--navy)"/>
      <rect x="400" y="545" width="38" height="660" fill="var(--cyan)"/>
      <path d="M0,1264 C150,1180 330,1130 480,1128 C660,1126 830,1180 976,1240 V1264 Z" fill="var(--cyan)"/>
      <path d="M0,1264 C150,1180 330,1130 480,1128 C660,1126 830,1180 976,1240" fill="none" stroke="var(--white)" stroke-width="5"/>
    </svg>

    <div class="brand"><span class="brand-dot"></span>BRIGHT PAGES LITERACY</div>

    <section class="tutors">
      <h2>Tutors</h2>
      <ul>
        <li>No special skills or degrees<br>needed — just a degree of caring!</li>
        <li>Training offered throughout<br>the year.</li>
        <li>Tutors meet students weekly at a<br>library.</li>
        <li>Instructional materials.</li>
        <li>Ongoing support available.</li>
      </ul>
      <p class="tagline">Teach an adult to read and you’ll<br>change a life forever.</p>
    </section>

    <section class="cta">
      <strong>Don’t waste a moment!</strong>
      Contact us today to learn more.
    </section>

    <div class="circle-photo circle-1" role="img" aria-label="Photo: a tutor and a student reading together"></div>
    <div class="circle-photo circle-2" role="img" aria-label="Photo: a tutor helping two adult learners at a table"></div>
    <div class="circle-photo circle-3" role="img" aria-label="Photo: smiling adult learners in a library"></div>

    <section class="intro">
      <h1>Volunteer</h1>
      <p class="first">Enrich a Life!</p>
      <p>Help an adult learn to read</p>
      <p>write or speak English</p>
    </section>

    <section class="students">
      <h2>Students</h2>
      <p class="lead">Students are adults in need of</p>
      <ul>
        <li>basic literacy skills</li>
        <li>pre-GED skills</li>
        <li>conversational English</li>
        <li>Tutoring is free of charge</li>
        <li>Tutoring is one-on-one</li>
        <li>Flexible scheduling during library hours</li>
        <li>Lessons focus on student goals</li>
      </ul>
      <p class="tagline">If you can read, you can tutor!</p>
    </section>

    <footer class="contact">
      <p>Volunteer Desk: 555-014-2290</p>
      <p>Riverton, Oakmere &amp; Lake Vale: 555-017-6634</p>
      <p class="mail">
        <svg width="28" height="18" viewBox="0 0 28 18" aria-hidden="true"><rect x="0" y="0" width="28" height="18" fill="var(--white)"/><path d="M1,1 L14,11 L27,1" fill="none" stroke="var(--cyan)" stroke-width="2"/></svg>
        tutors@brightpages.org
      </p>
    </footer>
  </div>
</div>
</body>
</html>
```